Zestra Design Prize - $10,000 tablet app design contest, Magazine Category

Zestra is a marketplace for uSlate App Templates (similar to PageLoom templates). We want you to design an app template for sale in our marketplace which targets B2B or B2C Magazine Apps (uSlate Apps created for examples such as Alumni magazine, employee magazine, sports magazine, fashion magazine etc).

It’s up to you to create pages or features for the App Template that you think are appropriate. Creativity will be rewarded! Here are some example pages or features that you could create:

• Contents
• Editor’s letter
• Event calendar
• News page
• Feature article
• Business articles
• Social media integration
• Animations and video

Your design should be Vibrant, Engaging and Contemporary. If you have an uSlate, download Zestra Viewer and download template examples in the download tab.

Your entry must include:
• A brief description of your template
• Preview images of all pages of your template

Attached to this project are free templates to help you get started with your design. We have included:
1. A free portfolio template for designers/photographers
2. Icons and artwork to use in your template
3. Blank pages template
4. Form template
5. Video ad template

If you are selected as a finalist you will be required to submit an .oproject file containing:
• Your LayoutCraft source files
• Preview images of your template
• All creative / stock assets used in the template (animations, video etc.)
• A text file with instructions on how to update the template
• A metadata .txt file containing template details and your information

How to enter:
1. Register at Marketplace and view the instructions under the welcome message https://marketplace.zestrahub.test/welcome
2. Download Zestra Editor: https://support.zestrahub.test/entries/58104926-zestra-editor
3. Use the free templates provided in this brief to create your designs and submit to ArtFlock
Updates

Reason: Due to the Christmas break we are extending the deadline of our competition. Thank you for time and effort - I will be providing feedback over the next couple of days! Best wishes, Melody

Hi All,

I have received many screenshots with some great designs! I just wanted to clarify that you are designing Zestra app templates including Zestra features and not just page designs?

Read Tips for First Time Zestrans to guide you through the template creation process

Before you start designing templates for Zestra Marketplace

·       Read the Quality Standards

·       Read the Copyright Information 

·       Use the Template Quality Checklist to ensure your template follows our guidelines. 

What should my project file contain?

·       A folder containing your source files, e.g. LayoutCraft. This must be named Source.

·       The Zestra content files. This must be named Bundle.

·       Instructions, explaining to a customer how to use your template.

Best wishes,

Melody

Reason: We are extending the competition by 7 days to give you more time!

Reason: We have received 3 complete designs for this contest so we are extending the deadline for 7 days Best wishes, Melody

Target Market(s)

Entrepreneurs who wish to create uSlate Apps by using our App design templates.

Industry/Entity Type

Fashion

Requirements
Must have
• You will need Zestra Editor to open the .oproject files attached to this brief. Get it here: https://support.zestrahub.test/entries/58104926-zestra-editor
Should not have
• • Low quality, fuzzy or blurry images
• Any stock images or content which you do not own the rights to
• Any material which could be considered inappropriate or offensive

```html
<!DOCTYPE html>
<html lang="en">
<head>
<meta charset="utf-8">
<title>Zestra Magazine Template – Second Article</title>
<link rel="stylesheet" href="https://fonts.googleapis.com/css2?family=Questrial&family=Poppins:wght@600;700&family=Crimson+Text:wght@400;700&display=swap">
<style>
  :root {
    --stage: #0c0c0c;
    --paper: #ffffff;
    --ink: #1f1f1f;
    --yellow: #ffe02b;
    --blue: #6f8ff0;
    --orange: #d95a2b;
    --white: #ffffff;
    --sans: "Questrial", "Century Gothic", sans-serif;
    --display: "Poppins", "Avant Garde", sans-serif;
    --serif: "Crimson Text", "Minion Pro", serif;
  }
  * { box-sizing: border-box; margin: 0; padding: 0; }
  html, body { width: 916px; height: 1200px; overflow: hidden; }
  body { background: var(--stage); position: relative; font-family: var(--sans); color: var(--ink); }

  .page { position: absolute; overflow: hidden; background: var(--paper); }
  .page--article-end { left: 16px; top: 0; width: 426px; height: 582px; display: flex; flex-direction: column; }
  .page--opener { left: 476px; top: 0; width: 424px; height: 582px; }
  .page--closing { left: 16px; top: 617px; width: 426px; height: 566px; padding: 6px 12px 0; display: flex; flex-direction: column; }

  .body-copy { font-size: 9px; line-height: 12.4px; letter-spacing: -0.05px; hyphens: auto; }
  .body-copy p + p { margin-top: 12px; }

  .pull-quote { font-family: var(--serif); font-size: 19px; line-height: 22px; color: var(--blue); hyphens: auto; }
  .pull-quote--orange { color: var(--orange); font-size: 17px; line-height: 23px; }

  .stripe-band { flex: none; height: 18px;
    background: repeating-linear-gradient(90deg, var(--ink) 0 4px, transparent 4px 10px); }
  .stripe-band--white { background: repeating-linear-gradient(90deg, var(--white) 0 4px, transparent 4px 10px); }
  .stripe-band--yellow { background: repeating-linear-gradient(90deg, var(--yellow) 0 4px, transparent 4px 10px); }

  /* article end page */
  .intro-row { flex: none; height: 124px; display: flex; gap: 12px; padding: 0 12px; overflow: hidden; align-items: flex-end; padding-bottom: 40px; }
  .intro-row .pull-quote { width: 176px; flex: none; }
  .intro-row .body-copy { flex: 1; }
  .article-end-copy { flex: none; padding: 0 12px; }
  .article-end-stripe { margin: 8px 12px 0; }
  .slideshow-hint { flex: none; font-family: var(--serif); font-weight: 700; font-size: 12px; line-height: 15px; padding: 6px 12px 6px; }
  .slideshow-image { flex: none; width: 426px; height: 283px;
    background: linear-gradient(90deg, #f08a60 0%, #ec8d68 55%, #c9876f 72%, #6f8a93 82%, #dfe4ea 100%); }
  .article-end-tail { flex: none; padding: 9px 12px 0; }

  /* opener page */
  .opener-photo { position: absolute; inset: 0;
    background: linear-gradient(160deg, #cfd6dc 0%, #b9c2c7 30%, #d7d5cf 60%, #c7c0b4 80%, #e4e0d8 100%); }
  .opener-title { position: absolute; left: 2px; top: -14px; font-family: var(--display); font-weight: 700;
    font-size: 86px; line-height: 72px; letter-spacing: -2px; color: var(--yellow); text-transform: lowercase; }
  .opener-intro { position: absolute; left: 9px; top: 146px; width: 194px; display: flex; flex-direction: column; }
  .opener-standfirst { font-family: var(--serif); font-size: 15.5px; line-height: 21px; color: var(--white); }
  .opener-intro .stripe-band { width: 114px; margin-top: 8px; }
  .byline { font-family: var(--serif); font-weight: 700; font-size: 12px; line-height: 15px; color: var(--orange); margin-top: 10px; }
  .yellow-column { position: absolute; left: 206px; top: 150px; width: 210px; height: 425px; background: var(--yellow);
    padding: 4px 4px 0 4px; overflow: hidden; font-size: 9px; line-height: 12.4px; letter-spacing: -0.05px; hyphens: auto; }
  .sub-heading { font-family: var(--display); font-weight: 700; font-size: 16px; line-height: 20px; letter-spacing: 0.3px; color: var(--ink); text-transform: uppercase; }

  /* closing page */
  .closing-heading { margin: 8px 0 5px; }
  .split-row { display: flex; gap: 10px; flex: none; }
  .split-row .body-copy { width: 212px; flex: none; }
  .split-row .pull-quote { flex: 1; margin-top: -5px; }
  .closing-copy { margin-top: 10px; flex: none; }
  .page--closing .stripe-band--yellow { margin-top: 10px; }

  .nav-button { position: absolute; top: 499px; width: 56px; height: 56px; display: flex; flex-direction: column;
    align-items: center; justify-content: center; text-align: center; font-size: 6.5px; line-height: 9px; }
  .nav-button strong { font-size: 9px; line-height: 10px; font-weight: 400; }
  .nav-button--contents { left: 12px; border-radius: 50%; background: var(--blue); color: var(--white); }
  .nav-button--cover { left: 81px; background: var(--yellow); color: var(--blue); }
  .author-credit { position: absolute; right: 10px; top: 500px; text-align: right; font-family: var(--serif); font-size: 12px; line-height: 16px; }
  .author-credit b { font-weight: 700; }
</style>
</head>
<body>

<section class="page page--article-end">
  <div class="intro-row">
    <div class="pull-quote">Sed rutrum dolor in orci cursus suscipit. Duis non mi urna. Vestibulum dictum arcu felis.”</div>
    <div class="body-copy">Duis non mi velit, tincidunt non sagittis id, porta et magna. Donec varius lacinia purus, a dapibus nunc lacinia a. Vivamus elementum porttitor massa at feugiat. Proin a elit arcu. Ut quis arcu sit amet nunc mollis gravida. Vivamus in consectetur risus. Aenean quis elit libero. In volutpat ante in ligula euismod egestas.</div>
  </div>
  <div class="body-copy article-end-copy">Curabitur arcu metus, vulputate rhoncus ullamcorper sed, facilisis id ipsum. Donec convallis, risus ac fringilla mattis, urna neque tincidunt arcu, quis viverra tellus felis eu lectus. Aliquam quis gravida diam. Vestibulum rhoncus volutpat purus rutrum ullamcorper. Phasellus sed consectetur nulla. Suspendisse fermentum ligula sed turpis varius tempus. Duis eleifend sagittis mi id egestas. Donec non diam a odio imperdiet vulputate. Aliquam tristique, dolor ac venenatis sagittis, mauris elit facilisis metus, in convallis justo nisi quis dolor. Class aptent taciti sociosqu ad litora torquent per conubia nostra, per inceptos himenaeos. Donec in nisl mauris. Nulla pellentesque ultrices sapien, porttitor ullamcorper sapien imperdiet non.</div>
  <div class="stripe-band article-end-stripe"></div>
  <div class="slideshow-hint">Swipe images to view slideshow.</div>
  <div class="slideshow-image" role="img" aria-label="Slideshow photograph of colourful modernist sculpture and architecture"></div>
  <div class="body-copy article-end-tail">Pellentesque tempus sodales neque eu convallis. Aenean felis dui, semper eget luctus sit amet, venenatis eu nisi. Quisque vulputate vulputate magna, eu euismod mi ullamcorper mollis. Donec sed erat risus. Vestibulum placerat eros sed mi adipiscing ut rhoncus erat rutrum.</div>
</section>

<section class="page page--opener">
  <div class="opener-photo" role="img" aria-label="Full-page photograph of a modernist building with orange and green painted forms and a lone figure"></div>
  <h1 class="opener-title">second<br>article</h1>
  <div class="opener-intro">
    <p class="opener-standfirst">Sed rutrum dolor in orci cursus suscipit. Duis non mi urna. Vestibulum dictum arcu felis. Donec nec est eget urna faucibus pharetra at eget mauris.</p>
    <div class="stripe-band stripe-band--white"></div>
    <p class="byline">Article by Arlo Quentin Vance<br>01/01/13</p>
  </div>
  <div class="yellow-column">
    <p>Praesent interdum eros id augue sagittis vehicula. Praesent rhoncus laoreet rutrum. Suspendisse sem ligula, porta placerat fermentum vel, sollicitudin at nulla. Sed iaculis, ante quis facilisis fermentum, dui erat sagittis sapien, sollicitudin vulputate est augue vel turpis. Etiam eu feugiat ante. Maecenas fermentum velit non mauris placerat vel vehicula felis dapibus. Proin eget justo ac tortor pharetra condimentum. Vivamus euismod justo id nisi eleifend aliquam consequat augue pretium. Vivamus hendrerit venenatis pretium. In dui massa, convallis ac pellentesque ac, aliquet congue tortor. Phasellus tempus ullamcorper ipsum, non egestas risus euismod ac. Cum sociis natoque penatibus et magnis dis parturient montes, nascetur ridiculus mus. Quisque ultricies fringilla mauris vel volutpat. Aenean feugiat fringilla lacus, eget aliquet massa placerat sit amet.</p>
    <h2 class="sub-heading" style="margin:6px 0 2px;">Sub-heading</h2>
    <p>Donec lacus mi, mollis in consectetur ut, lobortis vel sapien. Vestibulum ante ipsum primis in faucibus orci luctus et ultrices posuere cubilia Curae; Quisque mi velit, tincidunt non sagittis id, porta et magna. Donec varius lacinia purus, a dapibus nunc lacinia a. Vivamus elementum porttitor massa at feugiat. Proin a elit arcu. Ut quis arcu sit amet nunc mollis gravida. Vivamus in consectetur risus. Aenean quis elit libero. In volutpat ante in ligula euismod egestas.</p>
    <p style="margin-top:12px;">Curabitur arcu metus, vulputate rhoncus ullamcorper sed, facilisis id ipsum. Donec convallis.</p>
  </div>
</section>

<section class="page page--closing">
  <div class="body-copy">Pellentesque tempus sodales neque eu convallis. Aenean felis dui, semper eget luctus sit amet, venenatis eu nisi. Quisque vulputate vulputate magna, eu euismod mi ullamcorper mollis. Donec sed erat risus. Vestibulum placerat eros sed mi adipiscing ut rhoncus erat rutrum. Donec ac nulla sapien, tempor mattis justo. Aliquam ut mauris felis. Praesent tortor lacus, mollis eu sodales et, ultricies ullamcorper urna. Pellentesque sit amet molestie nulla. Praesent tristique ante enim, vel interdum dui.</div>
  <h2 class="sub-heading closing-heading">Sub-heading</h2>
  <div class="split-row">
    <div class="body-copy">Fusce ac mi arcu. Nulla facilisi. Donec ullamcorper venenatis ipsum, eget auctor dui varius a. Aenean semper vulputate tortor congue bibendum. Morbi hendrerit quam id massa aliquet non molestie augue sollicitudin. Nam quis eros est, vitae rutrum turpis. Donec hendrerit risus at nisi volutpat porttitor. Pellentesque lacinia venenatis dapibus. Maecenas ut mauris justo. Donec vulputate massa a lectus egestas egestas. Vivamus ut urna ante. Fusce in leo purus, eu adipiscing ipsum. Vivamus consectetur neque ac dui consequat convallis. Cras euismod magna vel dui faucibus quis egestas nisl fringilla.</div>
    <blockquote class="pull-quote pull-quote--orange">“Nulla mauris magna, suscipit at auctor adipiscing, placerat a magna. In eu massa ante, non ullamcorper quam. Suspendisse libero metus, varius id commodo a, euismod at sem.”</blockquote>
  </div>
  <div class="body-copy closing-copy">
    <p>In hac habitasse platea dictumst. Curabitur diam est, auctor eu elementum ac, vulputate eget enim. Mauris id erat ut elit iaculis tempus non in massa. In hac habitasse platea dictumst. Aliquam et libero at nulla pellentesque blandit. Sed nec magna vitae tortor fringilla posuere eu ut nisi. Integer consequat, nunc at venenatis tincidunt, ante massa lobortis velit, sed dictum nisi turpis ac justo. Duis pretium consequat convallis. Cras eget dui leo, quis fringilla mauris. Phasellus lacus felis, rhoncus eu egestas in, vehicula nec mi. Donec euismod rutrum dignissim. Integer laoreet vestibulum erat in viverra. Aliquam est enim, vestibulum sed gravida in, hendrerit non dui. Aenean a quam ligula, vel sollicitudin sem. Curabitur porta blandit aliquam.</p>
    <p>Nulla mauris magna, suscipit at auctor adipiscing, placerat a magna. In eu massa ante, non ullamcorper quam. Suspendisse libero metus, varius id commodo a, euismod at sem. Pellentesque in lacus arcu, sed vulputate felis. Cras justo urna, dapibus at dapibus vel, venenatis vitae mauris. Ut vulputate sodales tortor, ut suscipit est rhoncus ac. Etiam id ligula lectus. Maecenas mattis venenatis pharetra. Praesent nec erat non elit condimentum gravida eu ut nisl.</p>
  </div>
  <div class="stripe-band stripe-band--yellow"></div>
  <a class="nav-button nav-button--contents">return<strong>contents<br>page</strong></a>
  <a class="nav-button nav-button--cover">return<strong>cover<br>page</strong></a>
  <div class="author-credit">
    <p><b>Article by Arlo Quentin Vance &nbsp;/// &nbsp;&nbsp;01/01/13</b></p>
    <p style="margin-top:8px;">Insert contact details &amp;<br>brief biography if desired.</p>
  </div>
</section>

</body>
</html>
```